Brivora Collective Business Card Design

We need a business card design for Brivora Collective. We are a healthcare recruiting, wellness and education company. We partner with medical facilities to find quality candidates. We also offer free wellness courses.
The final design should communicate an emphasis on recruiting and wellness
The main purpose of the business card is to utilized it for networking events, give to hospitals, executives, VCs surgery centers and clinics. I want it to be sleek, clean, use of our brand colors and professional.

```html
<!DOCTYPE html>
<html lang="en">
<head>
<meta charset="utf-8">
<title>Brivora Collective — Business Card</title>
<link rel="stylesheet" href="https://fonts.googleapis.com/css2?family=Questrial&family=Noto+Serif:wght@400&display=swap">
<style>
  :root {
    --teal: #0b5e55;
    --teal-dark: #06463f;
    --bg-light: #4f7a74;
    --bg-dark: #1f4a45;
    --paper: #ffffff;
    --ink: #2b2b2b;
    --rule: #3c3c3c;
  }
  * { margin: 0; padding: 0; box-sizing: border-box; }
  html, body { width: 1200px; height: 876px; overflow: hidden; }
  body {
    background: radial-gradient(ellipse at 55% 35%, var(--bg-light) 0%, var(--bg-dark) 85%);
    font-family: "Questrial", sans-serif;
    position: relative;
  }
  .card {
    position: absolute;
    width: 520px;
    height: 297px;
    top: 290px;
    box-shadow: 0 18px 40px rgba(0,0,0,0.35);
  }
  .card--front { left: 60px; background: var(--paper); }
  .card--back { left: 620px; background: var(--teal); }

  .brand {
    display: flex;
    align-items: center;
    gap: 10px;
    color: var(--teal);
    font-size: 24px;
    letter-spacing: 0.5px;
    white-space: nowrap;
  }
  .brand__mark { width: 16px; height: 16px; background: currentColor; flex: none; }

  .card--front .brand { position: absolute; left: 26px; top: 120px; font-size: 22px; }
  .divider {
    position: absolute;
    left: 262px; top: 90px;
    width: 1px; height: 120px;
    background: var(--rule);
  }
  .contact { position: absolute; left: 286px; top: 92px; }
  .contact__name {
    font-family: "Noto Serif", serif;
    color: var(--teal);
    font-size: 22px;
    line-height: 1.1;
  }
  .contact__title { color: var(--ink); font-size: 13px; margin-top: 4px; }
  .contact__list { list-style: none; margin-top: 16px; }
  .contact__item {
    display: flex; align-items: center; gap: 8px;
    color: var(--ink); font-size: 13px; line-height: 1.7;
  }
  .contact__item svg { width: 12px; height: 12px; fill: var(--teal); flex: none; }
  .contact__phone { letter-spacing: 2.5px; }

  .card--back .pattern {
    position: absolute; inset: 0;
    background: linear-gradient(135deg, var(--teal) 0%, var(--teal-dark) 100%);
  }
  .card--back .brand {
    position: absolute; left: 50%; top: 50%;
    transform: translate(-50%, -50%);
    color: var(--paper);
    font-size: 28px;
  }
</style>
</head>
<body>
  <section class="card card--front" aria-label="Business card front">
    <div class="brand"><span class="brand__mark"></span>Brivora Collective</div>
    <div class="divider"></div>
    <div class="contact">
      <p class="contact__name">Marisol Quenby</p>
      <p class="contact__title">Co-Founder + CEO</p>
      <ul class="contact__list">
        <li class="contact__item">
          <svg viewBox="0 0 24 24" aria-hidden="true"><path d="M6.6 10.8a15 15 0 0 0 6.6 6.6l2.2-2.2a1 1 0 0 1 1-.25 11.4 11.4 0 0 0 3.6.57 1 1 0 0 1 1 1V20a1 1 0 0 1-1 1A17 17 0 0 1 3 4a1 1 0 0 1 1-1h3.5a1 1 0 0 1 1 1c0 1.25.2 2.45.57 3.57a1 1 0 0 1-.25 1z"/></svg>
          <span class="contact__phone">123 456 7890</span>
        </li>
        <li class="contact__item">
          <svg viewBox="0 0 24 24" aria-hidden="true"><path d="M2 5h20v14H2zm2 2v.4l8 5.2 8-5.2V7zm0 2.8V17h16V9.8l-8 5.2z"/></svg>
          <span>info@brivoracollective.com</span>
        </li>
        <li class="contact__item">
          <svg viewBox="0 0 24 24" aria-hidden="true"><circle cx="12" cy="12" r="10"/><path d="M2 12h20M12 2c3 3 3 17 0 20M12 2c-3 3-3 17 0 20" stroke="#fff" stroke-width="1.4" fill="none"/></svg>
          <span>www.brivoracollective.com</span>
        </li>
      </ul>
    </div>
  </section>

  <section class="card card--back" aria-label="Business card back">
    <div class="pattern" role="img" aria-label="Embossed tonal brand pattern in deep teal"></div>
    <div class="brand"><span class="brand__mark"></span>Brivora Collective</div>
  </section>
</body>
</html>
```